Now Leasing Banner

Looking for a banner that says the following information approx 4' x 30'

Now Leasing Maplewood Terrace 925-318-6054

Target Market(s)

Drive by traffic

Industry/Entity Type

Residential property management

Requirements
Must have
• Clear and readable from a distance

```html
<!DOCTYPE html>
<html lang="en">
<head>
<meta charset="utf-8">
<title>Now Leasing Banner</title>
<link rel="stylesheet" href="https://fonts.googleapis.com/css2?family=Anton&family=Arimo:wght@700&display=swap">
<style>
  :root {
    --brand-green: #116c3e;
    --paper-white: #ffffff;
  }
  html, body {
    margin: 0;
    padding: 0;
    width: 1200px;
    height: 160px;
    overflow: hidden;
    background: var(--paper-white);
  }
  .banner {
    display: block;
    width: 1200px;
    height: 160px;
  }
  .headline {
    font-family: "Anton", "Impact", sans-serif;
    font-size: 100px;
    fill: var(--paper-white);
  }
  .phone {
    font-family: "Arimo", "Arial", sans-serif;
    font-weight: 700;
    font-size: 34px;
    letter-spacing: 2px;
    fill: var(--brand-green);
  }
  .band { fill: var(--brand-green); }
  .frame-light { stroke: var(--paper-white); stroke-width: 1.5; fill: none; }
  .frame-dark { stroke: var(--brand-green); stroke-width: 1.5; fill: none; }
</style>
</head>
<body>
<svg class="banner" viewBox="0 0 1200 160" xmlns="http://www.w3.org/2000/svg" aria-label="Now Leasing Maplewood Terrace, 925-318-6054">
  <!-- header band -->
  <rect class="band" x="0" y="0" width="1200" height="120"/>
  <!-- footer strip -->
  <rect class="band" x="0" y="154" width="1200" height="6"/>

  <!-- inset frame: light over the band, dark over the white area -->
  <path class="frame-light" d="M19.6 120 V14 H1187 V120"/>
  <path class="frame-dark" d="M19.6 120 V154 M1187 120 V154"/>

  <text class="headline" x="43" y="101.5" textLength="1114" lengthAdjust="spacingAndGlyphs">NOW LEASING MAPLEWOOD TERRACE</text>
  <text class="phone" x="600" y="148" text-anchor="middle" textLength="288" lengthAdjust="spacingAndGlyphs">925-318-6054</text>
</svg>
</body>
</html>
```